Design some Business Cards for brightNode

I am looking for someone to design some business cards for my company brightNode. Our main colors are Orange and Light Blue (as per our logo - which is attached). We also use a blue background pattern on different things throughout the company (which is also attached).
The business card design must have 2 sides. The cards must look professional.
Good Luck :)

```html
<!DOCTYPE html>
<html lang="en">
<head>
<meta charset="utf-8">
<title>brightNode Business Cards</title>
<link rel="stylesheet" href="https://fonts.googleapis.com/css2?family=Questrial&display=swap">
<style>
  :root {
    --stage: #000000;
    --orange: #ff9c00;
    --ink: #3a3a48;
    --url-ink: #6e5a3c;
    --blue-light: #1a82d4;
    --blue-mid: #0f5eb0;
    --blue-deep: #0a3c86;
    --navy: #15254f;
    --sky: #2a9fe6;
    --white: #ffffff;
  }
  * { margin: 0; padding: 0; box-sizing: border-box; }
  html, body {
    width: 1136px;
    height: 1200px;
    overflow: hidden;
    background: var(--stage);
    font-family: "Questrial", "Century Gothic", sans-serif;
  }
  .card {
    position: absolute;
    overflow: hidden;
  }
  .card--front {
    left: 107px; top: 84px;
    width: 911px; height: 486px;
    background: var(--orange);
  }
  .card--back {
    left: 107px; top: 637px;
    width: 916px; height: 490px;
    background: radial-gradient(ellipse 70% 75% at 48% 42%, var(--blue-light) 0%, var(--blue-mid) 55%, var(--blue-deep) 100%);
  }
  .brand {
    position: absolute;
    display: flex;
    align-items: center;
  }
  .brand__dot {
    border-radius: 50%;
    background: var(--sky);
    flex: none;
  }
  .brand__name { white-space: nowrap; line-height: 1; }

  .card--front .brand { left: 190px; top: 182px; gap: 38px; }
  .card--front .brand__dot { width: 120px; height: 120px; }
  .card--front .brand__name { font-size: 58px; color: var(--ink); }

  .front__url {
    position: absolute;
    left: 0; right: 0; top: 414px;
    text-align: center;
    font-size: 30px;
    color: var(--url-ink);
    letter-spacing: 0.5px;
  }

  .card--back .brand { left: 64px; top: 84px; gap: 14px; }
  .card--back .brand__dot { width: 96px; height: 96px; background: var(--orange); }
  .card--back .brand__name { font-size: 40px; color: var(--navy); }

  .person {
    position: absolute;
    right: 71px; top: 94px;
    text-align: right;
    color: var(--white);
  }
  .person__name { font-size: 28px; line-height: 1.2; }
  .person__role { font-size: 18px; margin-top: 10px; }

  .contact {
    position: absolute;
    top: 352px;
    color: var(--white);
    font-size: 23px;
    line-height: 41px;
    white-space: nowrap;
  }
  .contact--left { left: 105px; }
  .contact--right { left: 426px; }
  .contact__label { display: inline-block; width: 50px; }

  .corner-arrow {
    position: absolute;
    left: 0; top: 0;
    width: 916px; height: 490px;
  }
</style>
</head>
<body>
  <section class="card card--front" aria-label="Card front">
    <div class="brand">
      <span class="brand__dot"></span>
      <span class="brand__name">brightNode</span>
    </div>
    <p class="front__url">www.brightnode.com.au</p>
  </section>

  <section class="card card--back" aria-label="Card back">
    <div class="brand">
      <span class="brand__dot"></span>
      <span class="brand__name">brightNode</span>
    </div>
    <div class="person">
      <p class="person__name">Tom Kessler</p>
      <p class="person__role">Director</p>
    </div>
    <div class="contact contact--left">
      <p><span class="contact__label">A :</span>Perth, Australia</p>
      <p><span class="contact__label">T :</span>321 654 987</p>
    </div>
    <div class="contact contact--right">
      <p><span class="contact__label">E :</span>info@brightnode.com</p>
      <p><span class="contact__label">W :</span>www.brightnode.com.au</p>
    </div>
    <svg class="corner-arrow" viewBox="0 0 916 490" aria-hidden="true">
      <polygon points="815,385 916,319 916,451" fill="var(--orange)"/>
    </svg>
  </section>
</body>
</html>
```